Home Inspection Flyer

Looking to have flyer designed that features our business, services, and our contact information. There are three of us. We are all business partners and do not have a company phone number. So each of us would need to be listed on flyer along with our individual phone number. Everything you could possibly need is on our website from logo to services and contact information. https://cedarlinehomereview.com/. If you could possible incorporate our company colors that would be great. You can find those in our logo top left hand side of website and attached. Please also include our homechekguild and nrva logos ( home inspector affiliations ) on brochure as well. Those can be found on website. Please feel free to reach out with any questions.
Thanks
Dale
Updates
Looking to get a few tri fold designs. All the ones submitted have been 8x11

```html
<!DOCTYPE html>
<html lang="en">
<head>
<meta charset="utf-8">
<title>Cedarline Home Review – Flyer</title>
<link rel="stylesheet" href="https://fonts.googleapis.com/css2?family=Montserrat:wght@400;600;700&display=swap">
<style>
  :root {
    --green: #8dc63f;
    --ink: #1a1a1a;
    --white: #ffffff;
    --backdrop: #e6e7e9;
    --footer: #231f20;
  }
  * { box-sizing: border-box; margin: 0; padding: 0; }
  html, body { width: 1082px; height: 1200px; overflow: hidden; background: var(--backdrop); }
  body { font-family: "Montserrat", sans-serif; color: var(--ink); }

  .flyer {
    position: absolute; left: 77px; top: 0;
    width: 928px; height: 1200px;
    background: var(--white); overflow: hidden;
  }
  .hero { position: absolute; left: 0; top: 0; width: 928px; height: 360px; }

  .brand { position: absolute; right: 40px; top: 48px; text-align: right; }
  .brand-name {
    display: flex; align-items: center; justify-content: flex-end; gap: 10px;
    font-weight: 700; font-size: 24px; letter-spacing: 0.5px; color: var(--ink); line-height: 1.1;
  }
  .brand-dot { width: 18px; height: 18px; border-radius: 50%; background: var(--green); }
  .brand-url { margin-top: 52px; font-size: 11.5px; font-weight: 600; }

  .headline {
    position: absolute; left: 51px; top: 379px;
    font-size: 27.5px; font-weight: 400; line-height: 35px; text-transform: uppercase;
  }
  .rule-dark { position: absolute; left: 51px; top: 499px; width: 106px; height: 3px; background: var(--ink); }

  .intro {
    position: absolute; left: 51px; top: 522px; width: 380px;
    color: var(--green); font-weight: 700; font-size: 17px; line-height: 22px; text-transform: uppercase;
  }
  .experts-title { position: absolute; left: 51px; top: 644px; font-size: 18.5px; font-weight: 700; }

  .expert { position: absolute; left: 49px; display: flex; align-items: center; }
  .avatar { width: 98px; height: 98px; border-radius: 50%; flex: none; }
  .avatar.lime { background: radial-gradient(circle at 50% 45%, #2a2a2a 38%, #c3de2a 70%, #8fcf3c 100%); }
  .avatar.blue { background: radial-gradient(circle at 50% 45%, #2a2a2a 38%, #2ab0e0 70%, #1d6fb0 100%); }
  .avatar.purple { background: radial-gradient(circle at 50% 45%, #2a2a2a 38%, #9b4fc4 70%, #6a2c9a 100%); }
  .expert-info { margin-left: 33px; font-weight: 700; font-size: 15px; line-height: 18.4px; }
  .rule-green { position: absolute; left: 51px; width: 49px; height: 2.5px; background: var(--green); }

  .service { position: absolute; left: 512px; width: 360px; }
  .service h3 { color: var(--green); font-size: 16.5px; font-weight: 700; text-transform: uppercase; }
  .service p { margin-top: 14px; font-size: 14.3px; line-height: 18.3px; font-weight: 400; }

  .panel { position: absolute; left: 0; top: 0; width: 928px; height: 1200px; pointer-events: none; }
  .panel-service { position: absolute; left: 512px; width: 360px; color: var(--white); }
  .panel-service h3 { font-size: 16.5px; font-weight: 700; text-transform: uppercase; }
  .panel-service p { margin-top: 2px; font-size: 14.3px; line-height: 18.3px; }

  .footer { position: absolute; left: 0; bottom: 0; width: 928px; height: 24px; background: var(--footer); }
</style>
</head>
<body>
<main class="flyer">
  <svg class="hero" viewBox="0 0 928 360" role="img" aria-label="Photo of an inspector holding a magnifying glass over a model house">
    <defs>
      <linearGradient id="heroTone" x1="0" y1="0" x2="1" y2="1">
        <stop offset="0" stop-color="#8a8b8f"/>
        <stop offset="0.55" stop-color="#b9a394"/>
        <stop offset="1" stop-color="#e7c9b5"/>
      </linearGradient>
    </defs>
    <polygon points="0,26 348,26 828,353 0,353" fill="url(#heroTone)"/>
    <line x1="351" y1="10" x2="476" y2="97" stroke="var(--ink)" stroke-width="5"/>
  </svg>

  <div class="brand">
    <div class="brand-name"><span class="brand-dot"></span><span>CEDARLINE<br>HOME REVIEW</span></div>
    <div class="brand-url">www.cedarlinehomereview.com</div>
  </div>

  <h1 class="headline">"The Go-2 Guys" for homeowners,<br>buyers, sellers, FSBOs,<br>real estate agents, &amp; contractors</h1>
  <div class="rule-dark"></div>

  <h2 class="intro">Home inspection in Southwest PA home inspection services with upfront pricing &amp; no hidden fees by Pittsburgh's</h2>

  <h2 class="experts-title">TALK TO AN EXPERT</h2>

  <div class="expert" style="top:706px">
    <div class="avatar lime" role="img" aria-label="Portrait of Warren Hollis"></div>
    <div class="expert-info">Warren Hollis<br>Co-Owner &amp; Principal Partner<br>Certified Home Inspector &amp;<br>Building Consultant<br>+000 000 000</div>
  </div>
  <div class="rule-green" style="top:829px"></div>

  <div class="expert" style="top:854px">
    <div class="avatar blue" role="img" aria-label="Portrait of Dale Brenner"></div>
    <div class="expert-info">Dale Brenner<br>Certified Home Inspector &amp;<br>Building Consultant<br>+000 000 000</div>
  </div>
  <div class="rule-green" style="top:977px"></div>

  <div class="expert" style="top:1005px">
    <div class="avatar purple" role="img" aria-label="Portrait of Owen Maddox"></div>
    <div class="expert-info">Owen Maddox<br>Co-Owner &amp; Principal Partner<br>Certified Home Inspector &amp;<br>Building Consultant<br>+000 000 000</div>
  </div>

  <section class="service" style="top:523px">
    <h3>Pest Inspection</h3>
    <p>Pest Inspection To Prevent Wood Destroying Insects that cause millions of dollars in property damage for Southwestern PA homes &amp; buildings</p>
  </section>
  <section class="service" style="top:670px">
    <h3>Radon Test (Ion Chamber)</h3>
    <p>Radon Is A Cancer-Causing, Radioactive Gas. You Can’t See Radon. You Can’t Smell It Or Taste It. Radon Is A Serious Problem For Buyers &amp; Sellers When Detected In Southwestern PA Homes &amp; Buildings.</p>
  </section>
  <section class="service" style="top:837px">
    <h3>Water Sample Test</h3>
    <p>Water Test For Private, Public &amp; Municipal Residential Water Supply Systems</p>
  </section>

  <svg class="panel" viewBox="0 0 928 1200" aria-hidden="true">
    <polygon points="487,958 928,958 928,1176 451,1176" fill="var(--green)"/>
  </svg>
  <section class="panel-service" style="top:975px">
    <h3>Septic Dye Test</h3>
    <p>Septic Dye Test Can Expose Unhealthy Leaks &amp; Inadequacies In Your Waste System</p>
  </section>
  <section class="panel-service" style="top:1062px">
    <h3>Well Flow Test</h3>
    <p>Well Flow Test Can Determine If The Well Produces Enough Water To Safely Supply Your Household</p>
  </section>

  <div class="footer"></div>
</main>
</body>
</html>
```